meridale partners business card

Architectural firm business card
Updates

Please note:

corporate colour black+yellow are the only elements to be kept.
NO OTHER ELEMENT TO BE REUSED FROM PREVIOUS BUSINESS CARD.
Thank you.

Dear Everyone,

Thank you for your participation. I have upload the KBSO+ logo again for incoporate in the card. in tif and pdf format.

Thank you 

I keep getting request for the logo file. Does everyone has the same problem?

I cannot do much, because the file is upload to the website server. I can't seem to see it either.

The logo file is now working. Please download. I check it myself. Thank you everyone.

Dear All,

Thank you for all the hard work. There are a lot of great work. Due to current commitment with work, I am unable to review them just yet. I will do so next week and advise everyone also. Thank you again. Best regards

Dear All,

Thank you for your participation. There are a lot of good design. Unfortunately, I can only select one. All the best. This is definitely a good crowd to work with. Thank you everyone again.

Best regards

Target Market(s)

Corporate, commercial and institutional projects only

Industry/Entity Type

Business

Requirements
Must have
• elegant simple
double sided with coating
Member of Southland Guild of Draughtsmen (logo only)
corporate colour black and

LOGO FILE UPLOADED
Should not have
• should not be the same as current business card.
upload for reference information only.
font sans serif preferred.

```html
<!DOCTYPE html>
<html lang="en">
<head>
<meta charset="utf-8">
<title>meridale partners business card</title>
<link rel="stylesheet" href="https://fonts.googleapis.com/css2?family=Cabin:wght@400;500&display=swap">
<style>
  :root {
    --amber: #e9a23b;
    --ink: #0b0b0b;
    --paper: #ffffff;
    --font: "Cabin", "Helvetica Neue", Arial, sans-serif;
  }
  html, body {
    margin: 0;
    padding: 0;
    width: 927px;
    height: 1200px;
    overflow: hidden;
    background: var(--paper);
    font-family: var(--font);
  }
  .sheet {
    position: relative;
    width: 927px;
    height: 1200px;
  }
  .card {
    position: absolute;
    left: 21px;
    width: 883px;
    height: 527px;
    background: var(--amber);
    overflow: hidden;
  }
  .card--front { top: 33px; }
  .card--back { top: 580px; }
  .card__shapes {
    position: absolute;
    inset: 0;
    width: 100%;
    height: 100%;
  }
  .card__shapes circle { fill: var(--ink); }
  .card__text {
    position: absolute;
    margin: 0;
    white-space: nowrap;
    line-height: 1;
  }

  /* Front */
  .brand-name {
    left: 190px;
    top: 262px;
    color: var(--paper);
    font-size: 52px;
    font-weight: 400;
    line-height: 1.05;
    text-align: left;
  }
  .tagline {
    color: var(--paper);
    font-size: 15px;
    letter-spacing: 0.2px;
  }
  .card--front .tagline { left: 62px; top: 446px; }
  .member-badge {
    position: absolute;
    left: 762px;
    top: 414px;
    width: 54px;
    height: 54px;
    background: var(--paper);
  }

  /* Back */
  .person {
    left: 479px;
    top: 104px;
    color: var(--paper);
  }
  .person__name {
    font-size: 40px;
    font-weight: 400;
  }
  .person__post {
    font-size: 20px;
    color: var(--amber);
    margin-left: 4px;
  }
  .person__roles {
    position: absolute;
    left: 560px;
    top: 162px;
    width: 230px;
    text-align: center;
    color: var(--paper);
    font-size: 15px;
    line-height: 24px;
  }
  .person__roles small { font-size: 11px; }
  .firm {
    left: 65px;
    top: 345px;
    color: var(--paper);
  }
  .firm__name {
    display: block;
    font-size: 50px;
    font-weight: 400;
  }
  .firm__entity {
    display: block;
    font-size: 22px;
    margin-top: 8px;
  }
  .card--back .tagline { left: 65px; top: 447px; font-size: 14px; }
  .contact {
    position: absolute;
    left: 501px;
    top: 354px;
    color: var(--ink);
    font-size: 14px;
    line-height: 22px;
    font-style: normal;
  }
  .contact__building { font-size: 16px; }
</style>
</head>
<body>
<main class="sheet">

  <section class="card card--front" aria-label="Business card front">
    <svg class="card__shapes" viewBox="0 0 883 527" aria-hidden="true">
      <circle cx="100" cy="-220" r="485"/>
      <circle cx="980" cy="545" r="497"/>
    </svg>
    <p class="card__text brand-name">meridale<br>partners</p>
    <p class="card__text tagline">architects • urban designers • project managers</p>
    <div class="member-badge" role="img" aria-label="Member of the Southland Guild of Draughtsmen badge"></div>
  </section>

  <section class="card card--back" aria-label="Business card back">
    <svg class="card__shapes" viewBox="0 0 883 527" aria-hidden="true">
      <circle cx="990" cy="-250" r="505"/>
      <circle cx="-100" cy="580" r="520"/>
    </svg>
    <p class="card__text person">
      <span class="person__name">Daniel Hart</span><span class="person__post">kbso, spmi</span>
    </p>
    <p class="person__roles">
      Architect <small>(SG reg. no: 7314)</small><br>
      Director<br>
      M: 0491 570 156
    </p>
    <p class="card__text firm">
      <span class="firm__name">meridale</span>
      <span class="firm__entity">partners pty limited</span>
    </p>
    <p class="card__text tagline">architects • urban designers • project managers</p>
    <address class="contact">
      <span class="contact__building">Larkfield House</span><br>
      12 Corella Lane, Westbrook SG 3050<br>
      Tel: +612 5550 1842 • Fax: +612 5550 1843<br>
      email: mail@meridalepartners.com<br>
      web: www.meridalepartners.com.au
    </address>
  </section>

</main>
</body>
</html>
```